One page sales fact sheet for data consultancy company

We need a serious and professional looking 1-page fact sheet that we want to send over to potential clients via email.
The upper part should consists of a header, the client logo and 3 charts.
(1 chart with 5 datapoints / 1 chart with 3 bubbles and percentage in it, 1 chart with numbers and text)
In the lower part there should be some text description about our company and a big chart consisting of a table (see drawing).
See attached drawing to get a better understanding of the whole idea.
The fact sheet should be catchy but professional in the same way.
Colors your choice but classic, i.e. black/white/grey/blue
The contest winner can expect more work from us based on the winning design.
*Please note that the logo reflects our original logo style but is not our
actual company name for privacy reasons

```html
<!DOCTYPE html>
<html lang="en">
<head>
<meta charset="utf-8">
<title>Market Analysis Fact Sheet</title>
<link href="https://fonts.googleapis.com/css2?family=Oswald:wght@500;700&family=Montserrat:wght@400;500;700;800&display=swap" rel="stylesheet">
<style>
  :root{
    --brand-blue:#055a9c;
    --ink:#111111;
    --bar-grey:#636363;
    --grid:#c9c9c9;
    --pill-edge:#c4c4c4;
    --paper:#ffffff;
  }
  html,body{margin:0;padding:0;overflow:hidden;background:var(--paper);}
  .sheet{
    position:relative;width:973px;height:1200px;overflow:hidden;
    background:linear-gradient(135deg,#e4e4e4 0%,#f6f6f6 40%,#ececec 65%,#fafafa 100%);
    font-family:'Montserrat',sans-serif;color:var(--ink);
  }
  .abs{position:absolute;}
  .header-band{left:0;top:0;}
  .title{left:58px;top:28px;margin:0;font-family:'Oswald',sans-serif;font-weight:700;font-size:56px;line-height:1;color:var(--paper);letter-spacing:0.5px;white-space:nowrap;}
  .brand-name{left:583px;top:0;width:390px;height:173px;display:flex;align-items:center;justify-content:center;
    font-family:'Montserrat',sans-serif;font-weight:800;font-size:78px;color:var(--ink);letter-spacing:2px;padding-bottom:20px;box-sizing:border-box;}
  .chart-point{font-family:'Oswald',sans-serif;font-weight:500;font-size:20px;color:var(--brand-blue);white-space:nowrap;}
  .point-label{top:516px;width:80px;}
  .point-note{top:550px;width:80px;font-size:8.6px;line-height:13px;color:#222;}
  .section-heading{left:562px;top:215px;margin:0;font-weight:800;font-size:27px;letter-spacing:6.5px;color:var(--brand-blue);white-space:nowrap;}
  .stat-pill{height:47px;background:linear-gradient(#f4f4f4,#e4e4e4);border:1px solid var(--pill-edge);box-sizing:border-box;
    font-family:'Oswald',sans-serif;font-weight:700;font-size:28px;line-height:45px;color:var(--ink);
    white-space:nowrap;overflow:hidden;padding-left:26px;}
  .stat-pill.right{padding-left:44px;}
  .stat-icon{width:72px;height:72px;border-radius:50%;background:var(--brand-blue);border:3px solid var(--paper);box-sizing:border-box;
    box-shadow:0 0 0 1px #cfcfcf;display:flex;align-items:center;justify-content:center;}
  .summary{left:86px;top:814px;width:802px;margin:0;text-align:center;font-size:15px;line-height:21.5px;}
  .steps-band{left:0;top:928px;width:973px;height:272px;background:var(--brand-blue);}
  .steps-tab{left:0;top:928px;}
  .steps-title{left:331px;top:935px;width:311px;margin:0;text-align:center;font-weight:800;font-size:28px;color:var(--brand-blue);}
  .step-row{left:86px;width:802px;height:37px;border:1.5px solid #e9eef4;border-radius:3px;box-sizing:border-box;
    color:var(--paper);font-weight:700;font-size:23px;line-height:34px;white-space:nowrap;}
  .step-label{position:absolute;left:47px;top:0;}
  .step-divider{position:absolute;left:217px;top:6px;width:1.5px;height:22px;background:#dfe7f0;}
  .step-value{position:absolute;left:295px;top:0;font-weight:500;}
  .step-value.spaced{letter-spacing:14px;font-weight:700;}
</style>
</head>
<body>
<div class="sheet">

  <svg class="abs" width="973" height="1200" aria-hidden="true" style="left:0;top:0">
    <polygon points="583,0 973,0 973,173 613,173" fill="#ffffff"/>
  </svg>

  <svg class="abs header-band" width="580" height="134" aria-hidden="true">
    <polygon points="0,0 517,0 571,133 0,133" fill="var(--brand-blue)"/>
  </svg>
  <h1 class="abs title">MARKET ANALYSIS</h1>
  <div class="abs brand-name">VORDA</div>

  <svg class="abs" width="540" height="620" style="left:0;top:0" aria-label="Bar chart of five data points">
    <g stroke="var(--grid)" stroke-width="1">
      <line x1="94" y1="181" x2="520" y2="181"/><line x1="94" y1="226" x2="520" y2="226"/>
      <line x1="94" y1="272" x2="520" y2="272"/><line x1="94" y1="317" x2="520" y2="317"/>
      <line x1="94" y1="362" x2="520" y2="362"/><line x1="94" y1="408" x2="520" y2="408"/>
      <line x1="94" y1="453" x2="520" y2="453"/><line x1="94" y1="498" x2="520" y2="498"/>
    </g>
    <g fill="var(--bar-grey)">
      <rect x="131" y="181" width="47" height="317"/>
      <rect x="210" y="293" width="47" height="205"/>
      <rect x="289" y="398" width="47" height="100"/>
      <rect x="368" y="340" width="47" height="158"/>
      <rect x="448" y="251" width="47" height="247"/>
    </g>
    <g stroke="var(--brand-blue)" stroke-width="1.5">
      <line x1="94" y1="167" x2="94" y2="609"/>
      <line x1="94" y1="609" x2="520" y2="609"/>
    </g>
    <g font-family="Montserrat, sans-serif" font-size="8.5" fill="#111" text-anchor="end">
      <text x="91" y="184">141-160</text><text x="91" y="229">121-140</text>
      <text x="91" y="275">101-120</text><text x="91" y="320">81-100</text>
      <text x="91" y="365">61-80</text><text x="91" y="411">41-60</text>
      <text x="91" y="456">21-40</text><text x="91" y="501">0-20</text>
    </g>
  </svg>
  <div class="abs chart-point point-label" style="left:127px">Point 1</div>
  <div class="abs chart-point point-label" style="left:205px">Point 2</div>
  <div class="abs chart-point point-label" style="left:284px">Point 3</div>
  <div class="abs chart-point point-label" style="left:363px">Point 4</div>
  <div class="abs chart-point point-label" style="left:442px">Point 5</div>
  <div class="abs point-note" style="left:128px">Lorem ipsum dolor sit amet, consectetur</div>
  <div class="abs point-note" style="left:206px">Lorem ipsum dolor sit amet, consectetur</div>
  <div class="abs point-note" style="left:285px">Lorem ipsum dolor sit amet, consectetur</div>
  <div class="abs point-note" style="left:364px">Lorem ipsum dolor sit amet, consectetur</div>
  <div class="abs point-note" style="left:443px">Lorem ipsum dolor sit amet, consectetur</div>

  <h2 class="abs section-heading">PRODUCT TYPES</h2>
  <svg class="abs" width="973" height="620" style="left:0;top:0" aria-label="Donut charts of product types">
    <g font-family="Montserrat, sans-serif" font-weight="800" font-size="20" text-anchor="middle" fill="#111">
      <g transform="translate(616,355)">
        <circle r="73" fill="#fff" stroke="#cfcfcf"/>
        <circle r="55" fill="none" stroke="var(--brand-blue)" stroke-width="36" stroke-dasharray="201.6 400" transform="rotate(240)"/>
        <circle r="38" fill="#fff" stroke="#bfc9d3" stroke-width="1.5"/>
        <text y="7">40%</text>
      </g>
      <g transform="translate(822,355)">
        <circle r="73" fill="#fff" stroke="#cfcfcf"/>
        <circle r="55" fill="none" stroke="var(--brand-blue)" stroke-width="36" stroke-dasharray="230.4 400" transform="rotate(210)"/>
        <circle r="38" fill="#fff" stroke="#bfc9d3" stroke-width="1.5"/>
        <text y="7">30%</text>
      </g>
      <g transform="translate(616,528)">
        <circle r="73" fill="#fff" stroke="#cfcfcf"/>
        <circle r="55" fill="none" stroke="var(--brand-blue)" stroke-width="36" stroke-dasharray="283.2 400" transform="rotate(155)"/>
        <circle r="38" fill="#fff" stroke="#bfc9d3" stroke-width="1.5"/>
        <text y="7">20%</text>
      </g>
      <g transform="translate(816,528)">
        <circle r="73" fill="#fff" stroke="#cfcfcf"/>
        <circle r="55" fill="none" stroke="var(--brand-blue)" stroke-width="36" stroke-dasharray="316.8 400" transform="rotate(120)"/>
        <circle r="38" fill="#fff" stroke="#bfc9d3" stroke-width="1.5"/>
        <text y="7">10%</text>
      </g>
    </g>
  </svg>

  <div class="abs stat-pill" style="left:148px;top:651px;width:221px">20 VENDOR</div>
  <div class="abs stat-pill" style="left:148px;top:732px;width:387px">350,000 AVAILABLE ITEMS</div>
  <div class="abs stat-pill right" style="left:624px;top:651px;width:277px">750 PRODUCTS</div>
  <div class="abs stat-pill right" style="left:624px;top:732px;width:277px">40MLN IN SALES</div>

  <div class="abs stat-icon" style="left:75px;top:638px" aria-label="Vendors">
    <svg width="40" height="40" viewBox="0 0 40 40" fill="none" stroke="#fff" stroke-width="1.8">
      <circle cx="20" cy="9" r="4"/><circle cx="9" cy="13" r="3.2"/><circle cx="31" cy="13" r="3.2"/>
      <path d="M13 35V20a7 7 0 0 1 14 0v15M3 33V23a6 6 0 0 1 9-5M37 33V23a6 6 0 0 0-9-5M17 27v8M23 27v8"/>
    </svg>
  </div>
  <div class="abs stat-icon" style="left:75px;top:719px" aria-label="Available items">
    <svg width="40" height="40" viewBox="0 0 40 40" fill="none" stroke="#fff" stroke-width="3">
      <path d="M30 21v13H6V10h18"/><path d="M12 19l7 7L35 8"/>
    </svg>
  </div>
  <div class="abs stat-icon" style="left:560px;top:638px" aria-label="Products">
    <svg width="40" height="40" viewBox="0 0 40 40" fill="none" stroke="#fff" stroke-width="1.8">
      <rect x="4" y="24" width="14" height="12"/><rect x="18" y="24" width="16" height="12"/>
      <rect x="9" y="12" width="14" height="12"/><rect x="14" y="3" width="9" height="9"/>
      <path d="M11 24v4M26 24v4M16 12v4"/>
    </svg>
  </div>
  <div class="abs stat-icon" style="left:560px;top:719px" aria-label="Sales">
    <svg width="40" height="40" viewBox="0 0 40 40" fill="none" stroke="#fff" stroke-width="1.8">
      <path d="M4 20l8-8 6 5 10-10M23 7h5v5"/>
      <path d="M22 18v9M27 15v12M32 12v15"/>
      <path d="M4 30h8l6 3 10-4a2 2 0 0 1 2 3l-11 6H4"/>
    </svg>
  </div>

  <p class="abs summary">Lorem ipsum dolor sit amet, consectetur adipiscing elit, sed do eiusmod tempor incididunt ut labore et dolore magna aliqua. Ut enim ad minim veniam, quis nostrud exercitation ullamco laboris nisi ut aliquip ex ea commodo consequat. Duis aute irure dolor in reprehenderit in voluptate velit esse cillum dolore eu fugiat nulla pariatur.</p>

  <div class="abs steps-band"></div>
  <svg class="abs steps-tab" width="973" height="60" aria-hidden="true">
    <polygon points="331,0 642,0 614,52 359,52" fill="#ffffff"/>
  </svg>
  <h2 class="abs steps-title">STEPS</h2>

  <div class="abs step-row" style="top:999px"><span class="step-label">LABEL 1</span><span class="step-divider"></span><span class="step-value spaced">COMPETITORS</span></div>
  <div class="abs step-row" style="top:1041px"><span class="step-label">LABEL 2</span><span class="step-divider"></span><span class="step-value">USER LEVEL</span></div>
  <div class="abs step-row" style="top:1083px"><span class="step-label">LABEL 3</span><span class="step-divider"></span><span class="step-value">ENTRY LEVEL</span></div>
  <div class="abs step-row" style="top:1126px"><span class="step-label">LABEL 4</span><span class="step-divider"></span><span class="step-value">PERSONAL LEVEL</span></div>

</div>
</body>
</html>
```